Hotel Company Personal Business Card

This is a hotel business, personal business card. Need it sleek, professional, and sharp looking. I have a design attached that we can work with. My turnaround time is April 8th. I would need the cards by then. One side only color, the other side all details. This is flexible depending on the designs you come up with. I would like a boutique, unique, modern type of touch to the business card. Memorable type of card that people will want to keep.

Target Market(s)

Business professionals

Industry/Entity Type

Hospitality/Hotels & Resorts

Contact Information for Business Card

Name, email, phone number, address, and company name. Anything unique

Font styles to use
Serif
Sans Serif

Colors

Designer to choose colors to be used in the design.

Requirements
Nice to have
• Neutral colors. Eye popping logo. Sleek design. Boutique feel. Hint of color.

```html
<!DOCTYPE html>
<html lang="en">
<head>
<meta charset="utf-8">
<title>Harbor Lane Hotel Group – Business Card</title>
<link href="https://fonts.googleapis.com/css2?family=Lato:wght@400;700&display=swap" rel="stylesheet">
<style>
  :root {
    --backdrop: #3b3b3e;
    --card: #24252b;
    --ink: #e9e7e3;
    --accent: #8d7862;
    --rule: #b9b7b3;
  }
  * { margin: 0; padding: 0; box-sizing: border-box; }
  html, body {
    width: 1200px; height: 694px; overflow: hidden;
    background: var(--backdrop);
    font-family: "Lato", Arial, sans-serif;
  }
  .canvas {
    position: relative; width: 1200px; height: 694px;
    display: flex; align-items: center; justify-content: center; gap: 40px;
  }
  .card {
    position: relative; width: 540px; height: 310px;
    background: var(--card); border-radius: 22px;
    box-shadow: 0 14px 34px rgba(0,0,0,.35);
    color: var(--ink);
  }
  /* Front side */
  .card--front { display: flex; align-items: center; justify-content: center; }
  .brand { display: flex; align-items: center; gap: 16px; }
  .brand__mark { width: 18px; height: 18px; background: var(--accent); }
  .brand__name {
    font-weight: 700; font-size: 27px; letter-spacing: 4px;
    text-transform: uppercase; color: var(--ink); line-height: 1.2;
  }
  /* Back side */
  .brand--small { position: absolute; top: 44px; right: 36px; gap: 10px; }
  .brand--small .brand__mark { width: 11px; height: 11px; }
  .brand--small .brand__name { font-size: 15px; letter-spacing: 2.5px; }
  .person { position: absolute; left: 36px; top: 96px; }
  .person__name {
    color: var(--accent); font-size: 26px; font-weight: 400;
    letter-spacing: .5px; text-transform: uppercase;
  }
  .person__title { font-size: 17px; margin-top: 4px; }
  .divider {
    position: absolute; left: 36px; right: 36px; top: 170px;
    height: 1px; background: var(--rule);
  }
  .contact { position: absolute; left: 36px; top: 188px; list-style: none; }
  .contact__item {
    display: flex; align-items: center; gap: 12px;
    font-size: 16px; letter-spacing: .3px; margin-bottom: 9px;
  }
  .contact__icon { width: 20px; height: 20px; flex: none; }
  .address {
    position: absolute; right: 36px; top: 188px;
    text-align: right; font-size: 15px; line-height: 1.4;
    text-transform: uppercase; letter-spacing: .4px;
  }
</style>
</head>
<body>
<main class="canvas">
  <section class="card card--front" aria-label="Card front">
    <div class="brand">
      <span class="brand__mark"></span>
      <span class="brand__name">Harbor Lane<br>Hotel Group</span>
    </div>
  </section>

  <section class="card card--back" aria-label="Card back">
    <div class="brand brand--small">
      <span class="brand__mark"></span>
      <span class="brand__name">Harbor Lane<br>Hotel Group</span>
    </div>

    <div class="person">
      <h1 class="person__name">Marcus Hale</h1>
      <p class="person__title">Managing Director</p>
    </div>

    <div class="divider"></div>

    <ul class="contact">
      <li class="contact__item">
        <svg class="contact__icon" viewBox="0 0 20 20" aria-hidden="true">
          <circle cx="10" cy="10" r="10" fill="var(--accent)"/>
          <path d="M6.5 5.5l2 .2.8 2.2-1.2 1a6 6 0 0 0 3 3l1-1.2 2.2.8.2 2c-.8.9-2 1.1-3 .7A9 9 0 0 1 5.8 8.5c-.4-1 -.2-2.2.7-3z" fill="var(--card)"/>
        </svg>
        044-555 010 246
      </li>
      <li class="contact__item">
        <svg class="contact__icon" viewBox="0 0 20 20" aria-hidden="true">
          <circle cx="10" cy="10" r="10" fill="var(--accent)"/>
          <rect x="5" y="6.5" width="10" height="7" fill="var(--card)"/>
          <path d="M5 6.5l5 4 5-4" fill="none" stroke="var(--accent)" stroke-width="1"/>
        </svg>
        info@harborlane.com
      </li>
      <li class="contact__item">
        <svg class="contact__icon" viewBox="0 0 20 20" aria-hidden="true">
          <circle cx="10" cy="10" r="10" fill="var(--accent)"/>
          <circle cx="10" cy="10" r="5.5" fill="none" stroke="var(--card)" stroke-width="1.3"/>
          <path d="M4.5 10h11M10 4.5c-2.5 3-2.5 8 0 11M10 4.5c2.5 3 2.5 8 0 11" fill="none" stroke="var(--card)" stroke-width="1.1"/>
        </svg>
        www.harborlanehotels.com
      </li>
    </ul>

    <address class="address" style="font-style:normal">
      14 Alder Grove Dr.<br>Brookmere, N 4412
    </address>
  </section>
</main>
</body>
</html>
```